Rice Package Design

I want a modern 1 kg (Bulgur) Package Design (Our products are High quality)
for the Both sides front and back-side

Opened face Size : H:28.5 cm X W:20 cm *see Atachment1-size-file.pdf

package type *see attachment The-Package-type.png

Notes :
transparent area should be a to show the rice inside (20% of the design)
* use the logo on both sides
* you can add a slogan like (The Best Logumess or Original Products)
* elements needed to use in the design are attached for both faces and the nutrition facts table
(lorem text used I want you to replace all the text after awarding you)

```html
<!DOCTYPE html>
<html lang="tr">
<head>
<meta charset="utf-8">
<title>Kirsa Foods – Bulgur 1 kg Package, Back Side</title>
<link rel="stylesheet" href="https://fonts.googleapis.com/css2?family=Roboto:wght@400;700;900&family=Roboto+Condensed:wght@400;700&family=Noto+Sans+Arabic:wght@400;700&display=swap">
<style>
  :root{
    --page:#ffffff;
    --red:#e3141b;
    --green:#1f6a2c;
    --blue:#3a9fd8;
    --blue-dark:#1f5f9a;
    --blue-deep:#2f86c2;
    --gold:#d8a42a;
    --grain:#d9c489;
    --white:#ffffff;
    --ink:#1b3550;
  }
  *{box-sizing:border-box;margin:0;padding:0}
  html,body{width:1200px;height:920px;overflow:hidden;background:var(--page)}
  body{font-family:"Roboto",Arial,sans-serif;position:relative}

  .package{position:absolute;left:345px;top:27px;width:509px;height:866px;background:var(--blue);overflow:hidden}
  .band-top{position:absolute;left:0;top:0;width:100%;height:55px;background:var(--red)}
  .band-bottom{position:absolute;left:0;bottom:0;width:100%;height:52px;background:var(--red)}
  .upper{position:absolute;left:0;top:55px;width:100%;height:287px;background:var(--green)}

  .window{position:absolute;left:134px;top:65px;width:240px;height:240px;border-radius:50%;
    border:8px solid var(--red);background:radial-gradient(circle at 45% 40%,#e6d49d,var(--grain) 60%,#c6ad6c)}

  .brand{position:absolute;top:38px;width:90px;text-align:center;color:var(--gold);
    font:700 11px/1.1 "Roboto",Arial,sans-serif;letter-spacing:.5px;text-transform:uppercase}
  .brand::before{content:"";display:block;width:44px;height:44px;margin:0 auto 5px;border-radius:50%;background:var(--gold)}
  .brand.left{left:22px}
  .brand.right{right:22px}

  .divider{position:absolute;left:250px;top:352px;width:0;height:454px;border-left:2px dashed var(--white)}

  .col-left{position:absolute;left:22px;top:360px;width:218px;color:var(--white)}
  .col-right{position:absolute;left:262px;top:360px;width:232px;height:446px;color:var(--white);
    display:flex;flex-direction:column}

  .pill{background:var(--white);border-radius:14px;height:28px;display:flex;align-items:center;padding:0 14px}
  .pill.ar{justify-content:flex-end;font:700 17px "Noto Sans Arabic",sans-serif;color:var(--blue-dark);margin-top:8px}
  .pill.tr{margin-top:44px;font:900 18px "Roboto",sans-serif;color:var(--red);letter-spacing:.5px}

  .products{margin-top:8px;width:100%;border-collapse:collapse;font:400 8.3px/1.38 "Roboto Condensed",sans-serif}
  .products td{padding:0 2px;white-space:nowrap}
  .products td.code{text-align:right}

  .note{margin-top:10px;font:400 7.6px/1.35 "Roboto Condensed",sans-serif}
  .bullets{margin-top:10px;padding-left:10px;font:400 7.4px/1.35 "Roboto Condensed",sans-serif}
  .bullets li{margin-bottom:6px}

  .contact{flex:none;border:2px solid rgba(255,255,255,.8);border-radius:14px;height:62px;display:flex;align-items:center;gap:10px;padding:0 10px}
  .contact .icon{width:34px;height:34px;flex:none}
  .contact .numbers{font:900 20px/1.15 "Roboto",sans-serif;color:var(--white)}
  .badges{flex:none;display:flex;gap:10px;margin:6px 0 0 6px}
  .badge{width:30px;height:30px;border-radius:50%;background:var(--white);opacity:.9}
  .small{font:400 7px/1.3 "Roboto Condensed",sans-serif;text-align:center;margin-top:2px}
  .reg{font:900 20px/1 "Roboto",sans-serif;text-align:center;margin:4px 0 3px}
  .claim{font:700 8.5px/1.25 "Roboto",sans-serif;text-align:center}
  .arabic{font:400 8px/1.45 "Noto Sans Arabic",sans-serif;text-align:right;direction:rtl;margin-top:3px}

  .nutrition{margin-top:4px;width:100%;border-collapse:collapse;background:var(--white);color:var(--ink);
    font:400 7px/1.25 "Roboto Condensed",sans-serif}
  .nutrition th{background:var(--blue-dark);color:var(--white);font-weight:700;padding:2px 3px;text-align:left}
  .nutrition td{padding:1px 3px;border-bottom:1px solid #c9dcea}
  .nutrition td+td{text-align:right}

  .footer-row{flex:none;margin-top:8px;display:flex;align-items:flex-start;gap:12px}
  .batch{width:150px;height:82px;background:var(--white);color:var(--ink);
    font:700 8px "Roboto Condensed",sans-serif;padding:6px 8px;display:flex;flex-direction:column;justify-content:space-between}
  .batch span{display:flex;align-items:center;gap:6px}
  .batch span::after{content:"";flex:1;border-bottom:1px solid #9fb6c8}
  .origin{writing-mode:vertical-rl;transform:rotate(180deg);height:82px;text-align:center;
    font:900 24px/1 "Roboto",sans-serif;color:var(--blue-deep);letter-spacing:1px}
</style>
</head>
<body>
  <div class="package">
    <div class="band-top"></div>
    <div class="upper">
      <div class="brand left">Kirsa Foods</div>
      <div class="window" role="img" aria-label="Transparent window showing the bulgur grains inside"></div>
      <div class="brand right">Kirsa Foods</div>
    </div>

    <div class="divider"></div>

    <section class="col-left">
      <div class="pill ar">منتجاتنا</div>
      <div class="pill tr">ÜRÜNLERIMIZ</div>
      <table class="products">
        <tr><td>Baldo Pirinç</td><td>Rice</td><td class="code">73.2082</td></tr>
        <tr><td>Osmancık Pirinç</td><td>Baldo Rice</td><td class="code">73.2083</td></tr>
        <tr><td>Basmati Pirinç</td><td>Long Grain Rice</td><td class="code">73.2084</td></tr>
        <tr><td>Jasmine Pirinç</td><td>Rice</td><td class="code">73.2085</td></tr>
        <tr><td>Pilavlık Bulgur</td><td>Coarse Bulgur</td><td class="code">73.2086</td></tr>
        <tr><td>Köftelik Bulgur</td><td>Fine Bulgur</td><td class="code">73.2087</td></tr>
        <tr><td>Kırmızı Mercimek</td><td>Red Lentils</td><td class="code">73.2088</td></tr>
        <tr><td>Yeşil Mercimek</td><td>Green Lentils</td><td class="code">73.2089</td></tr>
        <tr><td>Nohut</td><td>Chickpeas</td><td class="code">73.2090</td></tr>
        <tr><td>Kuru Fasulye</td><td>White Beans</td><td class="code">73.2091</td></tr>
        <tr><td>Barbunya</td><td>Cranberry Beans</td><td class="code">73.2092</td></tr>
        <tr><td>Mısır</td><td>Corn</td><td class="code">73.2093</td></tr>
        <tr><td>Aşurelik Buğday</td><td>Wheat Pudding</td><td class="code">73.2094</td></tr>
        <tr><td>Kuru Bakla</td><td>Broad Beans</td><td class="code">73.2095</td></tr>
      </table>
      <p class="note">Ürünlerimiz özenle seçilmiş ve doğal yollarla paketlenmiştir.</p>
      <ul class="bullets">
        <li>Serin ve kuru yerde, doğrudan güneş ışığından uzakta muhafaza ediniz.</li>
        <li>Please store in a cool, dry place away from direct sunlight.</li>
        <li>Açıldıktan sonra kapalı bir kapta saklayınız.</li>
        <li>Keep in a closed container after opening.</li>
      </ul>
    </section>

    <section class="col-right">
      <div class="contact">
        <svg class="icon" viewBox="0 0 24 24" aria-hidden="true"><circle cx="12" cy="12" r="12" fill="#fff"/><path d="M8.2 6.5l2 2.2-1.1 1.7a8 8 0 0 0 4.5 4.5l1.7-1.1 2.2 2-1.1 2.2c-5 .2-9.8-4.6-9.6-9.6z" fill="#1f5f9a"/></svg>
        <div class="numbers">05320001471<br>05320001472</div>
      </div>
      <div class="badges"><div class="badge"></div><div class="badge"></div></div>
      <p class="small">Gıda İşletmesi Kayıt Numarası</p>
      <p class="reg">TR-00-K-000123</p>
      <p class="claim">Ürünlerimiz Domuz Yağı İçermemektedir<br>Our Products Do Not Contain Lard</p>
      <p class="arabic">منتجاتنا لا تحتوي على دهن الخنزير ومحفوظة بطريقة صحية</p>
      <table class="nutrition">
        <tr><th>Besin Değerleri (100 g)</th><th>kcal</th><th>Prot.</th><th>Karb.</th></tr>
        <tr><td>Pirinç</td><td>360</td><td>7.1</td><td>79.0</td></tr>
        <tr><td>Yeşil Mercimek</td><td>352</td><td>24.6</td><td>63.0</td></tr>
        <tr><td>Kırmızı Mercimek</td><td>358</td><td>23.9</td><td>63.1</td></tr>
        <tr><td>Bulgur</td><td>342</td><td>12.3</td><td>75.9</td></tr>
        <tr><td>Nohut</td><td>364</td><td>19.3</td><td>60.7</td></tr>
        <tr><td>Kuru Fasulye</td><td>333</td><td>23.4</td><td>60.3</td></tr>
        <tr><td>Mısır</td><td>365</td><td>9.4</td><td>74.3</td></tr>
      </table>
      <p class="arabic">يحفظ في مكان بارد وجاف بعيدا عن أشعة الشمس المباشرة</p>
      <div class="footer-row">
        <div class="batch">
          <span>Üretim Tarihi :</span>
          <span>Son Kul. Tarihi :</span>
          <span>Parti No :</span>
          <span>Ağırlık : 1 kg</span>
        </div>
        <div class="origin">Turkey</div>
      </div>
    </section>

    <div class="band-bottom"></div>
  </div>
</body>
</html>
```